Company or website name
- StepTrova
- Links to the website
- www.steptrova.com
- Describe your company and organization and target audience
- Dance Class finder website  Primary target audience : Dance enthusiasts Goal: To allow dance enthusiasts to search for dance classes and studios in their immediate area that offers the dance classes they desire at specific time and days w/o having to deal with the hassle of searching through every studio's dance schedule  Secondary target audience: Dance Instructors Goal: To allow dance instructors to network with studios, create a following of dance students, educate the public on the classes they instruct (ie. What class, when, where, etc...).  Tertiary target audience: Dance Studios Goal: To give dance studios organizational tools that will allow them to manage their business and schedule better.
- The design should have the following
- Colors: Red, grey, purple  Logo: Silhouette of dancers in movement practicing different forms of dance. Logo will be background to "StepTrova" lettering.  "StepTrova" lettering: Letters placed together without spacing or adding characters in place of letters. I would like this to "Pop"
- Other Facts

```html
<!DOCTYPE html>
<html lang="en">
<head>
<meta charset="utf-8">
<title>StepTrova – Find Your Dance Classes</title>
<link rel="stylesheet" href="https://fonts.googleapis.com/css2?family=Open+Sans:wght@300;400;600;700&display=swap">
<style>
:root{
  --night:#1d1124;
  --night-deep:#150a1c;
  --magenta:#9e1d5b;
  --magenta-dark:#8a174f;
  --violet:#9a5ad2;
  --violet-line:#7a3fb0;
  --brand:#8c3cc4;
  --ink:#222;
  --muted:#777;
  --rule:#dcdcdc;
  --paper:#f4f4f4;
  --white:#fff;
}
*{box-sizing:border-box;margin:0;padding:0}
html,body{width:1200px;height:2523px;overflow:hidden}
body{font-family:"Open Sans",sans-serif;background:var(--white);color:var(--ink);position:relative}
.abs{position:absolute}

/* Hero */
.hero{position:absolute;left:0;top:0;width:1200px;height:571px;background:radial-gradient(ellipse at 65% 40%,#3a2540 0%,var(--night) 55%,#120a17 100%)}
.brand{position:absolute;left:237px;top:40px;display:flex;align-items:center;gap:8px;font-weight:700;font-size:38px;color:var(--brand);letter-spacing:-0.5px}
.brand-dot{width:22px;height:22px;border-radius:50%;background:var(--brand)}
.account{position:absolute;top:54px;right:237px;display:flex;gap:6px}
.account a{display:block;height:21px;line-height:21px;padding:0 12px;font-size:10px;color:var(--white);text-decoration:none}
.account .login{background:var(--magenta)}
.account .register{background:var(--violet)}
.main-nav{position:absolute;left:237px;top:120px;width:726px;height:30px;background:var(--violet);border-bottom:3px solid var(--violet-line);display:flex}
.main-nav a{flex:1;text-align:center;line-height:28px;font-size:12px;color:var(--white);text-decoration:none}
.main-nav a.current{background:var(--magenta);flex:0 0 83px}
.hero h1{position:absolute;left:237px;top:260px;font-size:40px;font-weight:700;color:var(--white);letter-spacing:1px}
.hero .lead{position:absolute;left:237px;top:338px;font-size:31px;font-weight:300;color:var(--white);line-height:37px}
.btn{display:block;background:var(--violet);border-bottom:3px solid var(--violet-line);color:var(--white);text-align:center;text-decoration:none}
.hero .btn{position:absolute;left:237px;top:450px;width:158px;height:32px;line-height:30px;font-size:15px}
.hero-photo{position:absolute;left:600px;top:172px;width:300px;height:399px;background:radial-gradient(ellipse at 50% 45%,#d9d4dc 0%,#8e8494 35%,rgba(40,25,45,0) 70%)}

/* Finder */
.finder{position:absolute;left:0;top:571px;width:1200px;height:95px;background:var(--magenta)}
.finder h2{position:absolute;left:237px;top:32px;font-size:22px;font-weight:400;color:var(--white)}
.filters{position:absolute;left:489px;top:32px;display:flex;gap:1px}
.filter{width:94px;height:31px;background:var(--white);font-size:11px;color:#888;padding-left:12px;line-height:31px;position:relative}
.filter::after{content:"";position:absolute;right:10px;top:13px;border:4px solid transparent;border-top:5px solid #444}

/* Studios */
.studios{position:absolute;left:0;top:666px;width:1200px;height:402px;background:var(--paper)}
.studio{position:absolute;top:31px;width:158px}
.studio-photo{width:158px;height:158px;background:linear-gradient(160deg,#5a5350 0%,#2b2624 60%,#1c1816 100%)}
.studio h3{margin-top:18px;font-size:11px;font-weight:600;color:var(--ink)}
.studio p{margin-top:7px;font-size:10px;line-height:15px;color:var(--muted)}
.studio a{display:block;margin-top:8px;font-size:11px;color:var(--magenta);text-decoration:none}
.studios .rule{position:absolute;left:237px;top:314px;width:726px;height:1px;background:var(--rule)}
.pager{position:absolute;left:510px;top:348px;display:flex;gap:7px}
.pager span{height:21px;min-width:22px;padding:0 6px;line-height:21px;text-align:center;font-size:10px;color:#999;background:var(--white)}
.pager span.on{background:#999;color:var(--white)}

/* Events */
.events-title{position:absolute;left:236px;top:1124px;font-size:24px;font-weight:400}
.events-rule{position:absolute;left:237px;width:726px;height:1px;background:var(--rule)}
.event{position:absolute;left:237px;width:726px;height:126px}
.event .date{position:absolute;left:0;top:55px;font-size:10px;font-weight:600}
.event .date span{font-weight:400}
.event .thumb{position:absolute;left:122px;top:27px;width:62px;height:62px;border-radius:50%;background:radial-gradient(circle,#a39a93 0%,#4a3f3a 60%,#2a2220 100%)}
.event .when{position:absolute;left:216px;top:16px;font-size:8px;color:#888}
.event .when b{color:var(--violet);font-weight:600}
.event h4{position:absolute;left:216px;top:32px;font-size:11px;font-weight:600}
.event p{position:absolute;left:216px;top:50px;width:380px;font-size:10px;line-height:15px;color:var(--muted)}
.event .divider{position:absolute;left:630px;top:23px;width:1px;height:62px;background:var(--rule)}
.event .btn{position:absolute;left:661px;top:45px;width:65px;height:22px;line-height:20px;font-size:10px;border-bottom-width:2px}
.view-all{position:absolute;left:237px;top:1711px;font-size:11px;color:var(--magenta);text-decoration:none}

/* Why */
.why{position:absolute;left:0;top:1785px;width:1200px;height:345px;background:linear-gradient(90deg,#6b4a82 0%,#8a6a9e 35%,#7e5d95 60%,#6a4880 100%);text-align:center;color:var(--white)}
.why h2{margin-top:60px;font-size:31px;font-weight:700}
.why p{margin:22px auto 0;width:660px;font-size:20px;font-weight:300;line-height:30px}
.why .btn{width:160px;height:33px;line-height:31px;margin:22px auto 0;font-size:15px}

/* Footer */
.footer{position:absolute;left:0;top:2130px;width:1200px;height:393px;background:var(--night-deep);text-align:center;color:var(--violet)}
.footer-nav{margin-top:61px;font-size:11px}
.footer-nav a{color:var(--violet);text-decoration:none}
.footer-nav a.current{color:var(--magenta)}
.footer-nav .sep{color:#777;margin:0 12px}
.contact{margin-top:24px;font-size:11px;line-height:19px}
.social{display:flex;justify-content:center;gap:8px;margin-top:22px}
.social span{width:30px;height:30px;border-radius:50%;background:var(--magenta)}
.footer .brand{position:static;justify-content:center;margin-top:26px;font-size:36px}
.copy{margin-top:8px;font-size:10px}
</style>
</head>
<body>

<header class="hero">
  <div class="brand"><span class="brand-dot"></span>StepTrova</div>
  <div class="account"><a class="login" href="#">Login</a><a class="register" href="#">Register</a></div>
  <nav class="main-nav">
    <a class="current" href="#">Home</a><a href="#">About Us</a><a href="#">Classes</a><a href="#">Upcoming Events</a><a href="#">Studio Reviews</a><a href="#">Gallery</a><a href="#">Contact Us</a>
  </nav>
  <h1>LET’S DANCE</h1>
  <p class="lead">find your dance classes with<br>ease and no hassle</p>
  <a class="btn" href="#">Join Us Now</a>
  <div class="hero-photo" role="img" aria-label="Photo of a dancer in a flowing white dress on a pole"></div>
</header>

<section class="finder">
  <h2>Dance Classes Finder</h2>
  <div class="filters">
    <div class="filter">State</div><div class="filter">City</div><div class="filter">Type</div><div class="filter">Level</div><div class="filter">Day</div>
  </div>
</section>

<section class="studios">
  <article class="studio" style="left:237px"><div class="studio-photo" role="img" aria-label="Photo of two dancers performing"></div><h3>ABC Dance Studio</h3><p>Ballet, Contemporary Dance, Aerial Dance, Zumba, Street Dance</p><a href="#">View Details</a></article>
  <article class="studio" style="left:426px"><div class="studio-photo" role="img" aria-label="Photo of two dancers performing"></div><h3>ABC Dance Studio</h3><p>Ballet, Contemporary Dance, Aerial Dance, Zumba, Street Dance</p><a href="#">View Details</a></article>
  <article class="studio" style="left:616px"><div class="studio-photo" role="img" aria-label="Photo of two dancers performing"></div><h3>ABC Dance Studio</h3><p>Ballet, Contemporary Dance, Aerial Dance, Zumba, Street Dance</p><a href="#">View Details</a></article>
  <article class="studio" style="left:805px"><div class="studio-photo" role="img" aria-label="Photo of two dancers performing"></div><h3>ABC Dance Studio</h3><p>Ballet, Contemporary Dance, Aerial Dance, Zumba, Street Dance</p><a href="#">View Details</a></article>
  <div class="rule"></div>
  <div class="pager"><span class="on">1</span><span>2</span><span>3</span><span>4</span><span>...</span><span>Last</span></div>
</section>

<h2 class="events-title">Upcoming &nbsp;Events</h2>
<div class="events-rule" style="top:1179px"></div>

<article class="event" style="top:1179px"><div class="date">08 December <span>2017</span></div><div class="thumb" role="img" aria-label="Photo of a dancer"></div><div class="when"><b>Wednesday</b> | 10 : 00 am - 05 : 00 pm</div><h4>Tango Beginners Course and Party</h4><p>Lorem ipsum is simply dummy text of &nbsp;the printing at Lorem Park, Abcdef Street, Lorem City, Ipsum State</p><div class="divider"></div><a class="btn" href="#">Read More</a></article>
<div class="events-rule" style="top:1305px"></div>
<article class="event" style="top:1305px"><div class="date">08 December <span>2017</span></div><div class="thumb" role="img" aria-label="Photo of a dancer"></div><div class="when"><b>Wednesday</b> | 10 : 00 am - 05 : 00 pm</div><h4>Tango Beginners Course and Party</h4><p>Lorem ipsum is simply dummy text of &nbsp;the printing at Lorem Park, Abcdef Street, Lorem City, Ipsum State</p><div class="divider"></div><a class="btn" href="#">Read More</a></article>
<div class="events-rule" style="top:1431px"></div>
<article class="event" style="top:1431px"><div class="date">08 December <span>2017</span></div><div class="thumb" role="img" aria-label="Photo of a dancer"></div><div class="when"><b>Wednesday</b> | 10 : 00 am - 05 : 00 pm</div><h4>Tango Beginners Course and Party</h4><p>Lorem ipsum is simply dummy text of &nbsp;the printing at Lorem Park, Abcdef Street, Lorem City, Ipsum State</p><div class="divider"></div><a class="btn" href="#">Read More</a></article>
<div class="events-rule" style="top:1557px"></div>
<article class="event" style="top:1557px"><div class="date">08 December <span>2017</span></div><div class="thumb" role="img" aria-label="Photo of a dancer"></div><div class="when"><b>Wednesday</b> | 10 : 00 am - 05 : 00 pm</div><h4>Tango Beginners Course and Party</h4><p>Lorem ipsum is simply dummy text of &nbsp;the printing at Lorem Park, Abcdef Street, Lorem City, Ipsum State</p><div class="divider"></div><a class="btn" href="#">Read More</a></article>
<div class="events-rule" style="top:1683px"></div>
<a class="view-all" href="#">View All Upcoming Events</a>

<section class="why" role="img" aria-label="Blurred photo of a dance class in motion, tinted purple">
  <h2>Why Choose StepTrova</h2>
  <p>Sign up to StepTrova and be part of Lorem Ipsum has been the industry's standard dummy text ever since the 1500s, when an unknown printer took a galley of type</p>
  <a class="btn" href="#">Sign Up Here</a>
</section>

<footer class="footer">
  <nav class="footer-nav"><a class="current" href="#">Home</a><span class="sep">|</span><a href="#">About Us</a><span class="sep">|</span><a href="#">Classes</a><span class="sep">|</span><a href="#">Upcoming Events</a><span class="sep">|</span><a href="#">Studio Review</a><span class="sep">|</span><a href="#">Gallery</a><span class="sep">|</span><a href="#">Contact Us</a></nav>
  <div class="contact">Contact Address<br>Lorem Building, Lorem Ipsum Street, ABC City, State, 234567<br>email: query@steptrova.com<br>phone: 123 456 7890</div>
  <div class="social"><span role="img" aria-label="Social network link"></span><span role="img" aria-label="Social network link"></span><span role="img" aria-label="Social network link"></span></div>
  <div class="brand"><span class="brand-dot"></span>StepTrova</div>
  <div class="copy">StepTrova © 2017 | All Rights Reserved</div>
</footer>

</body>
</html>
```